High-end executive coaching group needs a 2 page digital flyer

We need a 2 page digital flyer for a high end leadership coaching offering for global leaders in healthcare. The flyer will advertise a new service (an elite senior leadership coaching group) for senior leaders in the healthcare industry from around the world.
The flyer should be upmarket, professional and minimalist in style to meet the expectations of my professional market (very senior doctors and executives).
The design should be based on my existing logo and brand, see my landing page: www.lantavereadvisory.com
The key elements needed are
1) An editable PDF which we can update as we revise the specific details of the offering. The text and draft design for this is attached.
2) The banner image should be high quality but abstract. It can be based on the landing page of my website (the two ripple effects) but does not need to strictly adhere to this.
3) The logo placement of the Lantavere Advisory delta sign should be discreet so that it does not dominate
4) The small logos of our professional accrediting organisations should be discreetly placed at the end and should not dominate. They might work best as mono icons in a footer (e.g. blue on a white background, or white on blue.
5) Please find enclosed a previous flyer as an example of a similar style we have used for more junior professionals. The design worked quite well, although we now need a more upmarket version for our senior executives.
Updates

Please note this design specifically needs to use existing branding and images from my website: lantavereadvisory.com. We are definitely not looking for stock "leadership team" images for this high-end brochure.

Target Market(s)

Senior global leaders in the healthcare industry

Industry/Entity Type

Leading business schools & Healthcare industry.

Font styles to use
Other font styles liked:
• Operetta (selective use for heading) and Sofia Pro (body text)

Colors
0054AA
0677BA
7BADD7
CADEEF
E8F1F8

Requirements
Must have
• Clean minimalist and high professionally look that directly speaks to the interests and perspectives of senior leader leaders in healthcare. It also needs very clear call to action sections
Nice to have
• Effective presentation of the two bios and photographs. These need to look impressive, but should not dominate.
Should not have
• Loud and bold colours, large use of logos.

```html
<!DOCTYPE html>
<html lang="en">
<head>
<meta charset="utf-8">
<title>Lantavere Advisory – Analytic Coaching Group flyer</title>
<link rel="stylesheet" href="https://fonts.googleapis.com/css2?family=Figtree:ital,wght@0,400;0,500;0,600;0,700;1,400&family=Playfair+Display:ital,wght@0,400;0,700;1,700&family=Cormorant+Garamond:wght@400&display=swap">
<style>
:root{
  --navy:#27367c;
  --blue:#1f4fa3;
  --blue-text:#1d4fa5;
  --blue-mid:#3d66be;
  --sky:#7badd7;
  --mist:#cadeef;
  --pale:#e8f1f8;
  --ink:#2b2f3a;
  --paper:#ffffff;
  --page2-bg:#f5f7fb;
  --backdrop:#e6e7ea;
}
*{box-sizing:border-box;margin:0;padding:0}
html,body{width:1050px;height:1200px;overflow:hidden}
body{background:var(--backdrop);font-family:"Figtree",sans-serif;color:var(--ink);position:relative}
.sheet{position:absolute;top:250px;width:495px;height:700px;box-shadow:0 6px 18px rgba(0,0,0,.18);overflow:hidden}
.sheet--front{left:20px}
.sheet--back{left:535px}
.page{position:absolute;left:0;top:0;width:752px;height:1063px;transform:scale(.6582);transform-origin:0 0;background:var(--paper);overflow:hidden}
.abs{position:absolute}

/* front page */
.hero{left:0;top:0;width:752px;height:455px;background:radial-gradient(circle at 78% 22%,#e6f0f9 0,#cfe1f1 35%,#b7d2ea 70%,#a9c9e6 100%)}
.hero-facet{left:0;top:0;width:752px;height:455px}
.brand-name{left:280px;top:105px;width:250px;text-align:center;font-family:"Cormorant Garamond",serif;font-weight:400;font-size:38px;line-height:.92;color:#3b5fa8}
.photo-frame{left:28px;top:190px;width:340px;height:232px;border:1px solid rgba(255,255,255,.75)}
.photo{left:40px;top:200px;width:316px;height:212px;background:linear-gradient(135deg,#d9c8b4,#b9a58f 45%,#6f7f78 100%)}
.headline{right:42px;top:340px;text-align:right;color:var(--blue-text);font-family:"Playfair Display",serif;line-height:1.1}
.headline .lead{font-style:italic;font-weight:700;font-size:38px}
.headline .soft{font-size:30px;font-weight:400}
.headline .big{font-style:italic;font-weight:700;font-size:44px}
.band{left:0;top:455px;width:752px;height:52px;background:var(--blue);color:#fff;font-size:14.5px;line-height:1.45;padding:7px 0 0 40px}
.band-chevron{left:650px;top:470px;width:102px;height:100px}
.col-left{left:40px;top:532px;width:300px}
.col-left h2,.col-right h2{font-size:18px;font-weight:700;color:var(--blue-text);line-height:1.15;margin-bottom:24px}
.col-left p{font-size:13px;line-height:1.22;margin-bottom:14px}
.details{left:0;top:802px;width:330px;height:200px;background:#f2f6fb;border-top:1px solid #dbe6f2;border-right:1px solid #dbe6f2;padding:22px 0 0 40px;font-size:13px;line-height:1.22}
.details dl{display:grid;grid-template-columns:100px 1fr;row-gap:6px}
.details dt{color:var(--blue-text)}
.details .accent{color:var(--blue-text)}
.col-right{left:368px;top:530px;width:360px}
.benefits{list-style:none}
.benefits li{position:relative;padding-left:36px;font-size:13px;line-height:1.42;margin-bottom:12px}
.benefits li svg,.questions li svg{position:absolute;left:12px;top:3px;width:15px;height:12px}
.benefits b{color:var(--blue-text);font-weight:600;font-size:14px}
.quote{left:358px;top:870px;width:394px;height:136px;background:var(--navy);color:#fff;text-align:center;padding:20px 14px 0;font-size:13px;line-height:1.3}
.signature{font-family:"Playfair Display",serif;font-style:italic;font-weight:700;font-size:18px;margin-top:8px;letter-spacing:.3px}
.cta-bar{left:100px;top:1030px;width:410px;height:25px;background:var(--blue);color:#fff;font-size:13px;text-align:center;line-height:25px}

/* back page */
.page--back{background:var(--page2-bg)}
.tagline{left:0;top:0;width:752px;height:46px;background:#fff;color:var(--blue-text);font-weight:600;font-size:15.5px;text-align:center;line-height:46px}
.block-navy{left:0;top:46px;width:247px;height:320px;background:var(--navy)}
.block-navy::after{content:"";position:absolute;left:25px;top:28px;width:245px;height:262px;border:1px solid rgba(160,180,230,.5)}
.block-blue{left:507px;top:365px;width:245px;height:320px;background:var(--blue-mid)}
.block-blue::after{content:"";position:absolute;left:-25px;top:28px;width:245px;height:262px;border:1px solid rgba(200,215,245,.55)}
.portrait-frame{background:#fff;padding:8px;box-shadow:0 2px 6px rgba(0,0,0,.15)}
.portrait-frame--one{left:90px;top:85px;width:182px;height:245px}
.portrait-frame--two{left:480px;top:403px;width:185px;height:247px}
.portrait{width:100%;height:100%}
.portrait--one{background:linear-gradient(160deg,#7fa06a,#b7c8b0 40%,#3d5a95 100%)}
.portrait--two{background:linear-gradient(170deg,#1b1b1b,#3a2a22 55%,#d9a7a0 100%)}
.bio{font-size:13px;line-height:1.38}
.bio p{margin-bottom:20px}
.bio-name{font-family:"Playfair Display",serif;font-style:italic;font-weight:700;font-size:15px;color:var(--blue-text)}
.bio--one{left:302px;top:100px;width:420px}
.bio--two{left:38px;top:438px;width:412px;text-align:right}
.engage{left:22px;top:690px;width:350px}
.engage h3{font-family:"Playfair Display",serif;font-style:italic;font-weight:700;font-size:14.5px;line-height:1.2;color:var(--blue-text);margin-bottom:10px}
.questions{list-style:none}
.questions li{position:relative;padding-left:28px;font-size:13px;line-height:1.35;margin-bottom:10px}
.questions li svg{left:4px}
.quote--back{left:390px;top:684px;width:362px;height:142px;padding:14px 12px 0}
.badges{left:408px;top:848px;width:330px;height:48px;display:flex;align-items:center;justify-content:space-between}
.sea{left:0;top:930px;width:752px;height:133px;background:linear-gradient(180deg,#f0f3f7 0,#b9c5d2 45%,#51606f 100%)}
.cta-box{left:58px;top:950px;width:640px;height:113px;background:var(--blue);color:#fff;padding:12px 36px 0}
.cta-box .pair{display:flex;justify-content:space-between;font-size:13px;line-height:1.4}
.cta-box b{font-weight:600}
.url{left:255px;top:1036px;width:245px;height:27px;background:var(--navy);color:#fff;font-weight:600;font-size:14px;text-align:center;line-height:27px}
</style>
</head>
<body>

<section class="sheet sheet--front">
  <div class="page page--front">
    <div class="abs hero" role="img" aria-label="Abstract pale blue water ripple backdrop"></div>
    <svg class="abs hero-facet" viewBox="0 0 752 455" aria-hidden="true">
      <polygon points="0,160 500,455 0,455" fill="#ffffff" opacity=".18"/>
      <polygon points="230,170 380,455 230,455" fill="#7badd7" opacity=".12"/>
    </svg>
    <div class="abs brand-name">Lantavere<br>Advisory</div>
    <div class="abs photo-frame"></div>
    <div class="abs photo" role="img" aria-label="Photo of senior leaders in a group coaching conversation"></div>
    <div class="abs headline">
      <div><span class="lead">Elevate</span> <span class="soft">and</span> <span class="lead">Ignite</span></div>
      <div><span class="soft">Your</span> <span class="big">Leadership</span></div>
    </div>
    <div class="abs band">Transformative conversations for senior healthcare leaders.<br>Unlock purpose, engage authentically and amplify your leadership impact.</div>
    <svg class="abs band-chevron" viewBox="0 0 102 100" aria-hidden="true">
      <polygon points="102,10 30,50 102,90" fill="#fff"/>
      <polyline points="102,22 52,50 102,80" fill="none" stroke="#3d66be" stroke-width="9"/>
    </svg>

    <div class="abs col-left">
      <h2>Analytic Coaching Group<br>for Senior Leaders</h2>
      <p>As a senior leader in healthcare, you’re<br>constantly navigating challenges.</p>
      <p>But where do you turn for authentic<br>connections, reflection and personal growth?</p>
      <p>Rethink your leadership assumptions and<br>approach challenges with fresh creativity.</p>
      <p>Secure your spot in our exclusive Analytic<br>Coaching Group and ignite your leadership<br>potential.</p>
    </div>

    <div class="abs details">
      <dl>
        <dt>Dates:</dt><dd>7 February 2024 –<br>11 December 2024</dd>
        <dt>Time:</dt><dd>7:30am - 8:45am (UK time).</dd>
        <dt>Commitment:</dt><dd>Wednesdays, every 2 weeks</dd>
        <dt>Location:</dt><dd>Connect from anywhere by<br>Vidlink</dd>
        <dt>Cost:</dt><dd>Cost: £3350 [UK] €3900<br><span class="accent">[Europe] A$6530 [Australia]<br>Payment options available</span></dd>
      </dl>
    </div>

    <div class="abs col-right">
      <h2>Benefits to you</h2>
      <ul class="benefits">
        <li><svg viewBox="0 0 15 12"><path d="M1 6h11M8 2l4 4-4 4" fill="none" stroke="#3d66be" stroke-width="1.6"/></svg><b>Transformative conversations:</b> Engage in discussions that spark innovative leadership</li>
        <li><svg viewBox="0 0 15 12"><path d="M1 6h11M8 2l4 4-4 4" fill="none" stroke="#3d66be" stroke-width="1.6"/></svg><b>Peer insights:</b> Harness fresh insights from peers, enhancing your decision-making<br>and effectiveness</li>
        <li><svg viewBox="0 0 15 12"><path d="M1 6h11M8 2l4 4-4 4" fill="none" stroke="#3d66be" stroke-width="1.6"/></svg><b>Reimagined leadership:</b> Channel your creativity and redefine your leadership, personally and professionally</li>
        <li><svg viewBox="0 0 15 12"><path d="M1 6h11M8 2l4 4-4 4" fill="none" stroke="#3d66be" stroke-width="1.6"/></svg><b>Instant 360° insights:</b> Gain real-time feedback from trusted peers to enrich your leadership</li>
        <li><svg viewBox="0 0 15 12"><path d="M1 6h11M8 2l4 4-4 4" fill="none" stroke="#3d66be" stroke-width="1.6"/></svg><b>Lead authentically:</b> Develop effective strategies using the latest insights from group and leadership psychology</li>
      </ul>
    </div>

    <blockquote class="abs quote">
      “You bare your heart and share things you wouldn’t under normal circumstances. You get to know each other very quickly. There’s that sort of intense, shared experience that comes from speaking to each other’s lives.”
      <div class="signature">Sarah, Medical Director</div>
    </blockquote>

    <div class="abs cta-bar">Secure your spot now and ignite your leadership potential..</div>
  </div>
</section>

<section class="sheet sheet--back">
  <div class="page page--back">
    <div class="abs tagline">Expertly guided by insight, academic rigour and practical leadership strategies</div>

    <div class="abs block-navy"></div>
    <div class="abs portrait-frame portrait-frame--one"><div class="portrait portrait--one" role="img" aria-label="Portrait photo of Professor Adrian Holloway"></div></div>
    <div class="abs bio bio--one">
      <p><span class="bio-name">Professor Adrian Holloway</span> has 30 years’ experience developing leaders. An award-winning business school professor, group analyst and psychoanalytic psychotherapist, he has taught senior leadership programmes at Ashgrove University, Kingsmere College and Southbank University.</p>
      <p>His extensive leadership experience as a national health service clinical director and consultant psychotherapist inform his work as an ICCA accredited executive coach. With a PhD from Cresthaven College, University of Westmarch, he is an expert in melding psychological insights with strategic organisational change.</p>
    </div>

    <div class="abs block-blue"></div>
    <div class="abs portrait-frame portrait-frame--two"><div class="portrait portrait--two" role="img" aria-label="Portrait photo of Dr Helena Marsh"></div></div>
    <div class="abs bio bio--two">
      <p><span class="bio-name">Dr Helena Marsh</span> is a renowned psychoanalyst, group analyst, consultant psychiatrist and organisational consultant in the health sector. She has 20 years of leadership within the national health service, and she was also the National Director of Therapies for the Harrowgate Group, directing therapy services across 100 UK hospitals.</p>
      <p>She holds prominent positions as Chair of the Patient Safety Group, Chair of the Working Group on the Effect of Suicide and Homicide on Psychiatrists, and Vice Chair of the Psychotherapy Faculty at the Royal Guild of Psychiatrists.</p>
    </div>

    <div class="abs engage">
      <h3>Engage with global leaders, gain diverse insights<br>and forge lasting bonds. Explore questions such as:</h3>
      <ul class="questions">
        <li><svg viewBox="0 0 15 12"><path d="M1 6h11M8 2l4 4-4 4" fill="none" stroke="#3d66be" stroke-width="1.6"/></svg>What kind of leader do I aspire to be in the next chapter of my life and career?</li>
        <li><svg viewBox="0 0 15 12"><path d="M1 6h11M8 2l4 4-4 4" fill="none" stroke="#3d66be" stroke-width="1.6"/></svg>What unique qualities and actions do I offer that no one else can?</li>
        <li><svg viewBox="0 0 15 12"><path d="M1 6h11M8 2l4 4-4 4" fill="none" stroke="#3d66be" stroke-width="1.6"/></svg>How can I galvanise my personal strengths to inspire and motivate others?</li>
      </ul>
    </div>

    <blockquote class="abs quote quote--back">
      “Through this exceptional coaching, our leadership team elevated its performance to lead the hospital with greater clarity, cohesion and thoughtfulness. Not only do we provide a superior work environment for staff, but better care for our patients.”
      <div class="signature">John, CEO</div>
    </blockquote>

    <div class="abs badges" aria-label="Accreditation badges">
      <svg width="40" height="40" viewBox="0 0 40 40" aria-hidden="true"><circle cx="20" cy="20" r="18" fill="none" stroke="#1f4fa3" stroke-width="3"/></svg>
      <svg width="72" height="32" viewBox="0 0 72 32" aria-hidden="true"><rect x="2" y="6" width="68" height="20" rx="2" fill="#1f4fa3"/></svg>
      <svg width="66" height="32" viewBox="0 0 66 32" aria-hidden="true"><rect x="2" y="8" width="62" height="18" rx="2" fill="#27367c"/></svg>
      <svg width="88" height="28" viewBox="0 0 88 28" aria-hidden="true"><rect x="2" y="5" width="84" height="18" rx="2" fill="#27367c"/></svg>
    </div>

    <div class="abs sea" role="img" aria-label="Calm grey sea surface backdrop"></div>
    <div class="abs cta-box">
      <div class="pair">
        <div><b>Limited spots available</b><br><span style="display:block;margin-top:6px;line-height:1.2">Don’t miss this unique opportunity to<br>transform your leadership journey.</span></div>
        <div style="line-height:1.75">Book your free discovery call<br><b>adrian@lantavereadvisory.com</b><br><b>helenamarsh@postmail.net</b></div>
      </div>
    </div>
    <div class="abs url">www.lantavereadvisory.com</div>
  </div>
</section>

</body>
</html>
```